Packaging Design and Logo Project

I need to have a packaging design created as well as a logo that is incorporated in that packaging design, and one that I can use on my website.

The website is www.lunadrowse.com, so you can see and read about the product.

The product is a memory foam pillow, and will be packaged in a clear handle bag, like the following 2 examples. Inside the bag, and visible through the clear plastic, the packaging design is incorporated, like the following examples below.

For the package design, I would like to incorporate the “LunaDrowse” and “Traditional” pillow pictures from the homepage of my website. I would also like to include the words
“The Solution to Beautiful Skin”, “Stops Acne” , “Prevents Wrinkles” “and Much More”

The packaging design should look very professional and polished. For the logo design, that will be incorporated, this should also be professional and polished. I would also like the logo design provided to me in a separate file after I select the winner. I do not want the packaging design or the logo design to appear cartoonish.

Example 1 -

http://www.quorvix.com/picres?q=pillow+bag+package&hl=en&safe=active&rlz=1R2XXQT_enUS112&biw=1232&bih=565&tbm=isch&tbnid=kQw3TrabP2L_NxR:&imgrefurl=http://www.tradelumo.com/asia/pd/4418207/Pillow_Bag.html&docid=pRt7Zxk2_W9HQN&imgurl=http://img.tradelumo.com/cdimg/2204518/39051276/0/1174635820/Pillow_Bag.jpg&w=1023&h=768&ei=kw8pL2abMNcQxrhQpaz4DE&zoom=1

Example 2 -

http://www.quorvix.com/picres?q=pillow+bag+package&hl=en&safe=active&rlz=1R2XXQT_enUS112&biw=1232&bih=565&tbm=isch&tbnid=mTe8Kdpq4X_LnW:&imgrefurl=http://www.bzoq.com/product/6027413.html&docid=HwpXr38fN_KA2Q&imgurl=http://upload.bzoq.com/upload/Product/20122/Asia_Clear_PE_pillow_bag_cushion_bag201229047718253.jpg&w=551&h=421&ei=kw8pL2abMNcQxrhQpaz4DE&zoom=1

Reason: I would still like to see some more designs (pacakage and logo ideas). Thanks

Plastic

```html
<!DOCTYPE html>
<html lang="en">
<head>
<meta charset="utf-8">
<title>LunaDrowse Packaging Insert</title>
<link rel="stylesheet" href="https://fonts.googleapis.com/css2?family=Montserrat:wght@300;500;700&display=swap">
<style>
  :root {
    --lilac-top: #d0bde0;
    --lilac-bottom: #ad8bc4;
    --lilac-text: #b08ac8;
    --slate: #5f6e78;
    --slate-text: #7a8790;
    --white: #ffffff;
    --photo-light: #e9e2dc;
    --photo-mid: #c9b8a6;
    --photo-dark: #8f7f72;
  }
  html, body {
    margin: 0;
    padding: 0;
    overflow: hidden;
  }
  body {
    width: 1200px;
    height: 863px;
    font-family: "Montserrat", Arial, sans-serif;
  }
  .insert {
    position: relative;
    width: 1200px;
    height: 863px;
    overflow: hidden;
    background: linear-gradient(180deg, var(--lilac-top) 0%, var(--lilac-bottom) 100%);
  }
  .hero-panel {
    position: absolute;
    left: 51px;
    top: 48px;
    width: 1101px;
    height: 392px;
    background: var(--white);
    border-top-left-radius: 96px;
  }
  .brand-name {
    position: absolute;
    left: 108px;
    top: 160px;
    margin: 0;
    font-size: 66px;
    font-weight: 500;
    letter-spacing: -1px;
    color: var(--lilac-text);
    line-height: 1;
  }
  .tagline {
    position: absolute;
    left: 543px;
    top: 236px;
    margin: 0;
    font-weight: 300;
    font-size: 48px;
    line-height: 1.1;
  }
  .tagline-first {
    display: block;
    color: var(--lilac-text);
  }
  .tagline-second {
    display: block;
    padding-left: 107px;
    color: var(--slate-text);
  }
  .feature-band {
    position: absolute;
    left: 0;
    top: 438px;
    width: 1200px;
    height: 188px;
    background: var(--slate);
  }
  .feature-list {
    position: absolute;
    left: 108px;
    top: 450px;
    margin: 0;
    padding: 0;
    list-style: none;
  }
  .feature-heading {
    font-size: 23px;
    font-weight: 700;
    color: var(--lilac-text);
    letter-spacing: 0.5px;
    margin-bottom: 10px;
  }
  .feature-item {
    font-size: 24px;
    font-weight: 700;
    color: var(--white);
    line-height: 45px;
  }
  .feature-item::before {
    content: "\2022";
    color: var(--lilac-text);
    margin-right: 8px;
  }
  .photo {
    position: absolute;
    top: 398px;
    width: 318px;
    height: 272px;
    border-radius: 72px 0 72px 0;
  }
  .photo-traditional {
    left: 480px;
    background: linear-gradient(160deg, var(--photo-mid) 0%, var(--photo-light) 55%, var(--white) 100%);
  }
  .photo-product {
    left: 834px;
    background: linear-gradient(200deg, var(--white) 0%, var(--photo-light) 45%, var(--photo-mid) 100%);
  }
  .photo-caption {
    position: absolute;
    top: 682px;
    margin: 0;
    font-size: 18px;
    font-weight: 500;
    color: var(--white);
  }
  .caption-traditional { left: 480px; }
  .caption-product { left: 834px; }
  .web-tab {
    position: absolute;
    left: 667px;
    top: 760px;
    width: 533px;
    height: 103px;
    background: var(--white);
    border-top-left-radius: 100px;
  }
  .web-address {
    position: absolute;
    right: 47px;
    top: 790px;
    margin: 0;
    font-size: 28px;
    font-weight: 700;
    color: var(--slate-text);
  }
  .web-address-name {
    color: var(--lilac-text);
  }
</style>
</head>
<body>
  <main class="insert">
    <div class="hero-panel"></div>

    <h1 class="brand-name">LunaDrowse</h1>

    <p class="tagline">
      <span class="tagline-first">The Solution</span>
      <span class="tagline-second">to Beautiful Skin</span>
    </p>

    <div class="feature-band"></div>

    <ul class="feature-list">
      <li class="feature-heading">MEMORY FOAM PILLOW</li>
      <li class="feature-item">Stops Acne</li>
      <li class="feature-item">Prevents Wrinkles</li>
      <li class="feature-item">and Much, Much More!</li>
    </ul>

    <div class="photo photo-traditional" role="img" aria-label="Photo of a woman sleeping face-down on a traditional pillow"></div>
    <div class="photo photo-product" role="img" aria-label="Photo of a woman sleeping on her back on the LunaDrowse memory foam pillow"></div>

    <p class="photo-caption caption-traditional">Traditional Pillow</p>
    <p class="photo-caption caption-product">LunaDrowse</p>

    <div class="web-tab"></div>
    <p class="web-address">www.<span class="web-address-name">LunaDrowse</span>.com</p>
  </main>
</body>
</html>
```